electrical company- Company name- Voltmark Trades, slogan- All installations and servicingcolours to stick roughly with logo- greys, blues, black, white. simple yet effective- logo to stand out and attention to name also (gareth). Modern design.

Industry/Entity Type

Business

Contact Information for Business Card

gareth WilliamsElectrician021 994 306info@voltmarktrades.co.nzwww.voltmarktrades.co.nzPO box 5367Palmerston North, 4472

```html
<!DOCTYPE html>
<html lang="en">
<head>
<meta charset="utf-8">
<title>Voltmark Trades – Business Card</title>
<link href="https://fonts.googleapis.com/css2?family=Open+Sans:wght@400;600&display=swap" rel="stylesheet">
<style>
  :root {
    --page-bg: #e6e3df;
    --card-white: #ffffff;
    --card-black: #000000;
    --brand-blue: #0c93cc;
    --brand-grey: #8a8a8a;
    --text-dark: #2b2b2b;
    --rule-grey: #9a9a9a;
  }
  * { margin: 0; padding: 0; box-sizing: border-box; }
  html, body {
    width: 1200px; height: 1000px; overflow: hidden;
    background: var(--page-bg);
    font-family: "Open Sans", Arial, sans-serif;
  }
  .canvas { position: relative; width: 1200px; height: 1000px; }

  .card {
    position: absolute; left: 265px; width: 665px; height: 397px;
    border-radius: 20px; overflow: hidden;
    box-shadow: 0 6px 16px rgba(0,0,0,0.25);
  }
  .card-front { top: 73px; background: var(--card-white); }
  .card-back { top: 532px; background: var(--card-black); }

  /* Brand mark */
  .brand-square { position: absolute; background: var(--brand-blue); }
  .card-front .brand-square { left: 92px; top: 30px; width: 112px; height: 112px; }
  .brand-name {
    position: absolute; font-weight: 600; color: var(--brand-blue);
    letter-spacing: 1px; text-transform: uppercase; white-space: nowrap;
  }
  .card-front .brand-name { left: 33px; top: 162px; font-size: 23px; }

  /* Contact block */
  .address {
    position: absolute; left: 33px; top: 224px;
    font-size: 16.5px; line-height: 22px; color: var(--text-dark);
  }
  .person { position: absolute; right: 32px; top: 220px; text-align: right; }
  .person-name { font-size: 22px; color: var(--brand-blue); line-height: 30px; }
  .person-role { font-size: 16.5px; color: var(--text-dark); line-height: 22px; }
  .rule {
    position: absolute; left: 33px; top: 280px; width: 601px; height: 2px;
    background: linear-gradient(to right, #e8e8e8, var(--rule-grey));
  }
  .contact-list { position: absolute; left: 33px; top: 297px; list-style: none; }
  .contact-list li {
    display: flex; align-items: center; gap: 8px;
    font-size: 16.5px; line-height: 26px; color: var(--text-dark);
  }
  .contact-list svg { width: 13px; height: 13px; fill: var(--brand-blue); }

  .side-tab {
    position: absolute; right: 0; top: 224px; width: 8px; height: 38px;
    background: var(--brand-blue); border-radius: 4px 0 0 4px;
  }
  .web-band {
    position: absolute; left: 0; top: 360px; width: 100%; height: 27px;
    background: linear-gradient(to right, var(--brand-blue) 88%, var(--brand-grey) 88%);
  }
  .web-band span {
    position: absolute; left: 33px; top: 1px;
    font-size: 17px; letter-spacing: 2px; color: #ffffff;
  }

  /* Back */
  .card-back .brand-square { left: 257px; top: 74px; width: 150px; height: 150px; }
  .card-back .brand-name {
    left: 0; width: 100%; text-align: center; top: 263px; font-size: 32px;
  }
  .slogan {
    position: absolute; left: 0; width: 100%; top: 346px;
    text-align: center; font-size: 18px; color: #ffffff;
  }
</style>
</head>
<body>
<main class="canvas">
  <section class="card card-front">
    <div class="brand-square"></div>
    <div class="brand-name">Voltmark Trades</div>

    <p class="address">PO box 8142<br>Palmerston North, 4472</p>
    <div class="person">
      <div class="person-name">Gareth Pemberly</div>
      <div class="person-role">Electrician</div>
    </div>
    <div class="side-tab"></div>
    <div class="rule"></div>

    <ul class="contact-list">
      <li>
        <svg viewBox="0 0 24 24" aria-hidden="true"><path d="M6.6 10.8a15.2 15.2 0 0 0 6.6 6.6l2.2-2.2a1 1 0 0 1 1-.25 11.4 11.4 0 0 0 3.6.57 1 1 0 0 1 1 1V20a1 1 0 0 1-1 1A17 17 0 0 1 3 4a1 1 0 0 1 1-1h3.5a1 1 0 0 1 1 1c0 1.25.2 2.45.57 3.57a1 1 0 0 1-.25 1z"/></svg>
        021 573 814
      </li>
      <li>
        <svg viewBox="0 0 24 24" aria-hidden="true"><path d="M2 5h20v14H2z M2 5l10 8 10-8" /></svg>
        info@voltmarktrades-example.co.nz
      </li>
    </ul>

    <div class="web-band"><span>www.voltmarktrades-example.co.nz</span></div>
  </section>

  <section class="card card-back">
    <div class="brand-square"></div>
    <div class="brand-name">Voltmark Trades</div>
    <p class="slogan">All installations and servicing</p>
  </section>
</main>
</body>
</html>
```